Electrical Engineering Business Card Design

I need a business card design for an engineering consulting company based in Orlando, FL. I have had a logo created which the files are attached. We work primarily in the theme park and entertainment market sector but do projects in all market sectors. We have been serving Central Florida since 1994 and continue to strive to serve our clients and provide outstanding designs.
Theme Park

```html
<!DOCTYPE html>
<html lang="en">
<head>
<meta charset="utf-8">
<title>Voltline Associates, PA – Business Card</title>
<link rel="stylesheet" href="https://fonts.googleapis.com/css2?family=Montserrat:wght@600;700;800&display=swap">
<style>
  :root {
    --canvas-bg: #e9e9e7;
    --lime: #8cc63f;
    --lime-light: #a3d65a;
    --charcoal: #3a3a3c;
    --charcoal-deep: #2f2f31;
    --paper: #f7f7f6;
    --band: #e6e6e5;
    --ink: #3b3b3d;
    --white: #ffffff;
    --contact: #e4e4e4;
  }
  * { margin: 0; padding: 0; box-sizing: border-box; }
  html, body { width: 1200px; height: 900px; overflow: hidden; }
  body {
    background: var(--canvas-bg);
    font-family: "Montserrat", sans-serif;
    position: relative;
  }
  .card {
    position: absolute;
    left: 337px;
    width: 525px;
    height: 300px;
    border-radius: 4px;
    overflow: hidden;
    box-shadow: 0 6px 18px rgba(0,0,0,0.18);
  }
  .card-back { top: 110px; background: linear-gradient(135deg, var(--lime) 0%, var(--lime-light) 100%); }
  .card-front { top: 490px; background: var(--paper); }
  .card-shapes { position: absolute; inset: 0; width: 100%; height: 100%; }

  .back-mark {
    position: absolute;
    left: 150px; top: 100px; width: 300px;
    text-align: center;
    color: var(--white);
  }
  .back-mark .initials { font-weight: 800; font-size: 64px; letter-spacing: 2px; line-height: 1; }
  .back-mark .company { font-weight: 700; font-size: 19px; margin-top: 10px; }

  .front-company {
    position: absolute; left: 36px; top: 74px;
    font-weight: 700; font-size: 21px; color: var(--ink);
  }
  .front-initials {
    position: absolute; left: 320px; top: 80px; width: 205px;
    text-align: center;
    font-weight: 800; font-size: 50px; line-height: 1; color: var(--white);
    letter-spacing: 2px;
  }
  .front-address {
    position: absolute; left: 36px; top: 155px;
    font-weight: 600; font-size: 18px; color: var(--ink);
  }
  .contacts {
    position: absolute; left: 24px; top: 220px;
    display: flex; gap: 28px;
    color: var(--contact); font-weight: 600; font-size: 15px;
  }
  .contact-list { list-style: none; }
  .contact-list li { display: flex; align-items: center; gap: 8px; line-height: 22px; }
  .icon { width: 13px; height: 13px; fill: var(--contact); flex: none; }
</style>
</head>
<body>

<section class="card card-back" aria-label="Card back">
  <svg class="card-shapes" viewBox="0 0 525 300" aria-hidden="true">
    <path d="M190 30 H505 Q522 30 516 47 L440 300 H95 L170 45 Q174 30 190 30 Z" fill="var(--charcoal)"/>
  </svg>
  <div class="back-mark">
    <div class="initials">VLA</div>
    <div class="company">Voltline Associates, PA</div>
  </div>
</section>

<section class="card card-front" aria-label="Card front">
  <svg class="card-shapes" viewBox="0 0 525 300" aria-hidden="true">
    <rect x="0" y="135" width="420" height="65" fill="var(--band)"/>
    <path d="M525 60 H405 Q388 60 382 76 L340 183 Q333 200 312 200 H0 V300 H525 Z" fill="var(--charcoal-deep)"/>
    <path d="M525 72 H342 Q328 72 323 85 L305 132 Q302 145 316 145 H525 Z" fill="var(--lime)"/>
  </svg>
  <div class="front-company">Voltline Associates, PA</div>
  <div class="front-initials">VLA</div>
  <div class="front-address">PO Box 480217 Orlando, FL 32857</div>
  <div class="contacts">
    <ul class="contact-list">
      <li><svg class="icon" viewBox="0 0 16 16"><path d="M3 2h3l1.5 4-2 1.2a8 8 0 0 0 3.3 3.3L10 8.5l4 1.5v3a1 1 0 0 1-1 1A12 12 0 0 1 2 3a1 1 0 0 1 1-1z"/></svg>407-555-0182</li>
      <li><svg class="icon" viewBox="0 0 16 16"><path d="M4 2h8v4H4z M1 7h14v6h-3v-3H4v3H1z M5 11h6v4H5z"/></svg>407-555-0147</li>
    </ul>
    <ul class="contact-list">
      <li><svg class="icon" viewBox="0 0 16 16"><path d="M1 3h14v10H1z M2 4v1l6 4 6-4V4z" fill-rule="evenodd"/></svg>voltline.dan@example.com</li>
    </ul>
  </div>
</section>

</body>
</html>
```